fernbolt website

commerce website to sell cookeries, brackets, mailboxes and to show off homes built. Modern Steel in design see kelvo rides web page to be like: https://www.kelvorides.com/en/ sorry its blue mantis hosting word press divi

must be able to add products to page

Target Market(s)

mainly western states of U.S.

Industry/Entity Type

Building Product

Coding

Coded - Design and coding required

Number of Pages Required

3 page

Font styles to use
Sans Serif

Colors

Designer to choose colors to be used in the design.

Requirements
Must have
• customers to be able to order products from page
• blue mantis hosting word press divi

```html
<!DOCTYPE html>
<html lang="en">
<head>
<meta charset="utf-8">
<title>Fernbolt — Modern Steel</title>
<link href="https://fonts.googleapis.com/css2?family=Montserrat:wght@400;500;600;700&family=Lato:wght@400;700&display=swap" rel="stylesheet">
<style>
:root{
  --brand:#4b5b8c;
  --brand-dark:#3f4e7c;
  --ink:#333;
  --muted:#666;
  --line:#dcdcdc;
  --star:#f0a020;
  --sale:#f39a1e;
  --white:#fff;
}
*{box-sizing:border-box;margin:0;padding:0}
html,body{width:1200px;height:3753px;overflow:hidden;background:var(--white)}
body{position:relative;font-family:'Lato',sans-serif;color:var(--ink)}
.abs{position:absolute}
.heading{font-family:'Montserrat',sans-serif}

/* nav */
.site-nav{left:0;top:0;width:1200px;height:85px;background:var(--brand)}
.brand{left:113px;top:18px;width:116px;text-align:center;color:var(--white);font-family:'Montserrat',sans-serif;font-weight:600;font-size:19px;letter-spacing:1px;display:flex;flex-direction:column;align-items:center;gap:6px}
.brand .mark{width:22px;height:22px;border-radius:50%;background:var(--white)}
.nav-link{top:39px;color:var(--white);font-family:'Montserrat',sans-serif;font-size:14px;letter-spacing:.3px}
.cart{left:1055px;top:32px}

/* hero */
.hero{left:0;top:85px;width:1200px;height:553px;background:linear-gradient(180deg,#5f8a3a 0%,#7a6a3e 35%,#d4822a 55%,#6d6a66 80%,#3a3a3a 100%)}
.hero-title{left:0;top:255px;width:1200px;text-align:center;color:var(--white);font-family:'Montserrat',sans-serif;font-weight:600;font-size:94px;text-shadow:0 3px 8px rgba(0,0,0,.5)}
.hero-dots{left:1107px;top:326px;display:flex;flex-direction:column;gap:9px}
.hero-dots span{width:14px;height:14px;border-radius:50%;background:var(--white)}

/* products */
.section-title{left:0;width:1200px;text-align:center;font-family:'Montserrat',sans-serif;font-weight:500;font-size:38px;color:#333}
.card{width:228px;height:332px;border:1px solid var(--line);background:var(--white);text-align:center}
.card.hover{box-shadow:0 2px 10px rgba(0,0,0,.25)}
.card .photo{left:44px;top:32px;width:140px;height:150px;border-radius:6px;background:radial-gradient(circle at 50% 40%,#555 0%,#222 45%,#fff 75%)}
.card .photo.wide{left:20px;top:45px;width:188px;height:120px;background:radial-gradient(ellipse at 50% 50%,#555 0%,#222 45%,#fff 75%)}
.card .name{left:0;width:100%;font-family:'Montserrat',sans-serif;font-size:17px;color:#444}
.card .price{left:0;width:100%;font-size:19px;color:#222}
.card .price s{margin-left:8px}
.card .stars{left:0;width:100%;color:var(--star);font-size:14px;letter-spacing:3px}
.card .desc{left:10px;width:208px;font-size:12px;line-height:19px;color:#444}
.tag{left:24px;top:16px;background:var(--brand);color:var(--white);font-size:14px;padding:4px 12px}
.ribbon{left:0;top:0;width:58px;height:58px}
.heart{left:93px;top:110px;width:40px;height:40px;border-radius:50%;background:var(--sale);display:flex;align-items:center;justify-content:center}

/* banner */
.banner{left:0;top:1711px;width:1200px;height:517px;background:linear-gradient(180deg,#6b7277 0%,#5a4a3c 40%,#3a2a20 70%,#c8641e 90%,#3a2418 100%)}
.welcome{left:205px;top:1841px;width:790px;height:293px;background:rgba(20,14,12,.78);text-align:center;color:var(--white)}
.welcome h2{margin-top:40px;font-family:'Montserrat',sans-serif;font-weight:600;font-size:56px}
.welcome p{margin-top:18px;font-size:18px;line-height:34px}

/* manufacturer */
.mfr-title{left:115px;top:2340px;font-family:'Montserrat',sans-serif;font-weight:500;font-size:40px;color:#333}
.mfr-text{left:118px;top:2420px;width:502px;font-family:'Montserrat',sans-serif;font-size:15.5px;line-height:34px;color:#555;text-align:justify}
.btn{left:115px;top:2655px;width:140px;height:50px;background:var(--brand);color:var(--white);font-family:'Montserrat',sans-serif;font-size:17px;display:flex;align-items:center;justify-content:center}
.mfr-photo{left:706px;top:2345px;width:292px;height:350px;border-radius:8px;background:radial-gradient(ellipse at 50% 30%,#444 0%,#1e1e1e 40%,#fff 72%)}

/* testimonials */
.t-card{top:2990px;width:264px;height:254px;background:var(--white);box-shadow:0 1px 6px rgba(0,0,0,.25);text-align:center}
.avatar{top:2938px;width:96px;height:96px;border-radius:50%;background:linear-gradient(160deg,#c9a27a,#7a5a40);border:3px solid var(--white)}
.quote{font-family:Georgia,serif;font-size:40px;color:#c8c8c8;line-height:1}
.t-text{left:50px;top:70px;width:180px;text-align:left;font-family:'Montserrat',sans-serif;font-size:15px;line-height:23px;color:#333}
.t-name{left:0;top:175px;width:100%;font-family:'Montserrat',sans-serif;font-style:italic;font-size:14px;color:#999}
.t-stars{left:0;top:207px;width:100%;font-size:20px;letter-spacing:3px;color:var(--star)}
.t-stars .off{color:#aaa}
.arrow{top:3107px}

/* footer */
.footer{left:0;top:3333px;width:1200px;height:420px;background:var(--brand)}
.foot-brand{left:191px;top:3363px;width:166px;color:var(--white);font-family:'Montserrat',sans-serif;font-size:26px;letter-spacing:1px;display:flex;flex-direction:column;align-items:center;gap:8px}
.foot-brand .mark{width:32px;height:32px;border-radius:50%;background:var(--white)}
.contact-row{left:196px;color:var(--white);font-weight:700;font-size:19px;display:flex;align-items:center;gap:14px}
.contact-row.small{font-size:16px}
.foot-col{top:3400px;list-style:none;font-family:'Montserrat',sans-serif;font-size:18px;color:#f2f2f2;line-height:36px}
.copyright{left:107px;top:3677px;font-family:Arial,sans-serif;font-size:13px;color:var(--white)}
.pay{left:861px;top:3670px;width:227px;height:56px;background:var(--white);display:flex;align-items:center;justify-content:space-around;padding:0 8px}
.pay span{width:46px;height:30px;border-radius:3px}
</style>
</head>
<body>

<!-- navigation -->
<header class="abs site-nav">
  <div class="abs brand"><span class="mark"></span>FERNBOLT</div>
  <span class="abs nav-link" style="left:272px">HOME</span>
  <span class="abs nav-link" style="left:347px">ABOUT</span>
  <span class="abs nav-link" style="left:427px">PRODUCTS</span>
  <span class="abs nav-link" style="left:537px">MANUFACTURING</span>
  <span class="abs nav-link" style="left:699px">PRODUCTS</span>
  <span class="abs nav-link" style="left:810px">CONTACT</span>
  <span class="abs nav-link" style="left:907px">NEW ARRIVALS</span>
  <svg class="abs cart" width="40" height="30" viewBox="0 0 40 30">
    <path d="M2 5h5l4 13h13l3-9H9" fill="none" stroke="#fff" stroke-width="2.5"/>
    <circle cx="13" cy="23" r="2.2" fill="#fff"/><circle cx="22" cy="23" r="2.2" fill="#fff"/>
    <circle cx="31" cy="6" r="6" fill="#fff"/><text x="31" y="9" font-size="8" text-anchor="middle" fill="#4b5b8c" font-family="Arial">0</text>
  </svg>
</header>

<!-- hero -->
<section class="abs hero" role="img" aria-label="Photo of a steel fire pit table with flames on a lawn"></section>
<h1 class="abs hero-title">Fernbolt</h1>
<div class="abs hero-dots"><span></span><span></span><span></span></div>

<!-- products -->
<h2 class="abs section-title" style="top:746px">Our Products</h2>

<article class="abs card" style="left:109px;top:891px">
  <div class="abs photo" role="img" aria-label="Black kettle grill on wheels"></div>
  <span class="abs tag">New</span>
  <div class="abs name" style="top:206px">PRODUCT NAME</div>
  <div class="abs price" style="top:239px">$69.99</div>
  <div class="abs stars" style="top:276px">★★★★★</div>
</article>

<article class="abs card" style="left:360px;top:891px">
  <div class="abs photo" role="img" aria-label="Black kettle grill with side handle"></div>
  <svg class="abs ribbon" viewBox="0 0 58 58"><path d="M0 0h58L0 58z" fill="#4b5b8c"/><text x="16" y="26" transform="rotate(-45 16 26)" font-size="11" fill="#fff" font-family="Lato">SALE</text></svg>
  <div class="abs name" style="top:206px">PRODUCT NAME</div>
  <div class="abs price" style="top:239px">$69.99</div>
  <div class="abs stars" style="top:276px">★★★★★</div>
</article>

<article class="abs card" style="left:609px;top:891px">
  <div class="abs photo" role="img" aria-label="Tall black kettle grill on three legs"></div>
  <svg class="abs ribbon" viewBox="0 0 58 58"><path d="M0 0h58L0 58z" fill="#f39a1e"/><text x="16" y="26" transform="rotate(-45 16 26)" font-size="11" fill="#fff" font-family="Lato">SALE</text></svg>
  <div class="abs name" style="top:206px">PRODUCT NAME</div>
  <div class="abs price" style="top:239px">$79.99</div>
  <div class="abs stars" style="top:276px">★★★★★</div>
</article>

<article class="abs card hover" style="left:859px;top:891px">
  <div class="abs photo" style="top:30px;height:130px" role="img" aria-label="Rectangular steel charcoal grill on legs"></div>
  <div class="abs heart"><svg width="18" height="16" viewBox="0 0 18 16"><path d="M9 15S1 10 1 5a4 4 0 0 1 8-1 4 4 0 0 1 8 1c0 5-8 10-8 10z" fill="#fff"/></svg></div>
  <svg class="abs ribbon" viewBox="0 0 58 58"><path d="M0 0h58L0 58z" fill="#f39a1e"/><text x="16" y="26" transform="rotate(-45 16 26)" font-size="11" fill="#fff" font-family="Lato">SALE</text></svg>
  <div class="abs name" style="top:196px">PRODUCT NAME</div>
  <p class="abs desc" style="top:223px">Lorem ipsum dolor sit amet, consectetur adipiscing elit,</p>
  <div class="abs price" style="top:272px">$42.22<s>$52.45</s></div>
  <div class="abs stars" style="top:302px">★★★★★</div>
</article>

<article class="abs card" style="left:109px;top:1277px">
  <div class="abs photo" role="img" aria-label="Portable stainless barrel grill"></div>
  <span class="abs tag" style="left:12px;top:18px">Stock</span>
  <div class="abs name" style="top:216px">PRODUCT NAME</div>
  <div class="abs price" style="top:252px">$299.99</div>
  <div class="abs stars" style="top:294px">★★★★★</div>
</article>

<article class="abs card" style="left:360px;top:1277px">
  <div class="abs photo" role="img" aria-label="Black box grill on tall legs"></div>
  <svg class="abs ribbon" viewBox="0 0 58 58"><path d="M0 0h58L0 58z" fill="#f39a1e"/><text x="16" y="26" transform="rotate(-45 16 26)" font-size="11" fill="#fff" font-family="Lato">SALE</text></svg>
  <div class="abs name" style="top:216px">PRODUCT NAME</div>
  <div class="abs price" style="top:252px">$99.99</div>
  <div class="abs stars" style="top:294px">★★★★★</div>
</article>

<article class="abs card" style="left:609px;top:1277px">
  <div class="abs photo wide" role="img" aria-label="Low tabletop grill with wooden handles"></div>
  <svg class="abs ribbon" viewBox="0 0 58 58"><path d="M0 0h58L0 58z" fill="#4b5b8c"/><text x="16" y="26" transform="rotate(-45 16 26)" font-size="11" fill="#fff" font-family="Lato">SALE</text></svg>
  <div class="abs name" style="top:216px">PRODUCT NAME</div>
  <div class="abs price" style="top:258px">$32.22<s>$41.45</s></div>
  <div class="abs stars" style="top:294px">★★★★★</div>
</article>

<article class="abs card" style="left:859px;top:1277px">
  <div class="abs photo" style="background:radial-gradient(circle at 50% 35%,#b33 0%,#333 45%,#fff 75%)" role="img" aria-label="Red and black cart grill with shelves"></div>
  <span class="abs tag" style="left:10px;top:12px">out of stock</span>
  <div class="abs name" style="top:216px">PRODUCT NAME</div>
  <div class="abs price" style="top:252px">$2,999.99</div>
  <div class="abs stars" style="top:294px">★★★★★</div>
</article>

<!-- welcome banner -->
<section class="abs banner" role="img" aria-label="Photo of a cast iron pot hanging over a camp fire pit"></section>
<div class="abs welcome">
  <h2>Welcome To&nbsp; Fernbolt</h2>
  <p>Lorem ipsum dolor sit amet, consectetur adipiscing elit, sed do eiusmod tempor<br>incididunt ut labore et dolore magna aliqua. Quis ipsum suspendisse ultrices gravida.<br>Risus commodo viverra maecenas accumsan lacus vel facilisis.</p>
</div>

<!-- manufacturer -->
<h2 class="abs mfr-title">Manufacturer</h2>
<p class="abs mfr-text">Lorem ipsum dolor sit amet, consectetur adipiscing elit, sed do eiusmod tempor incididunt ut labore et dolore magna aliqua. Quis ipsum suspendisse ultrices gravida. Risus commodo viverra maecenas accumsan lacus vel facilisis. labore et dolore magna aliqua. Quis ipsum suspendisse ultrices gravida. Risus commodo viverra maecenas accumsan lacus vel facilisis.</p>
<a class="abs btn">Read More</a>
<div class="abs mfr-photo" role="img" aria-label="Black steel box grill with skewers on tall legs"></div>

<!-- testimonials -->
<h2 class="abs section-title" style="top:2852px">Testimonials</h2>

<svg class="abs arrow" style="left:68px" width="28" height="28" viewBox="0 0 28 28"><circle cx="14" cy="14" r="12" fill="none" stroke="#4b5b8c" stroke-width="2"/><path d="M17 8l-7 6 7 6z" fill="#4b5b8c"/></svg>
<svg class="abs arrow" style="left:1105px" width="28" height="28" viewBox="0 0 28 28"><circle cx="14" cy="14" r="12" fill="none" stroke="#4b5b8c" stroke-width="2"/><path d="M11 8l7 6-7 6z" fill="#4b5b8c"/></svg>

<article class="abs t-card" style="left:147px">
  <span class="abs quote" style="left:16px;top:34px">“</span>
  <p class="abs t-text">Lorem ipsum dolor sit amet, consectetur adipiscing elit, sed do</p>
  <span class="abs quote" style="right:18px;top:150px">”</span>
  <div class="abs t-name">Nora Vell</div>
  <div class="abs t-stars">★★★★<span class="off">★</span></div>
</article>
<div class="abs avatar" style="left:231px" role="img" aria-label="Customer portrait"></div>

<article class="abs t-card" style="left:475px">
  <span class="abs quote" style="left:16px;top:34px">“</span>
  <p class="abs t-text">Lorem ipsum dolor sit amet, consectetur adipiscing elit, sed do</p>
  <span class="abs quote" style="right:18px;top:150px">”</span>
  <div class="abs t-name">Owen Tarly</div>
  <div class="abs t-stars">★★★★<span class="off">★</span></div>
</article>
<div class="abs avatar" style="left:559px" role="img" aria-label="Customer portrait"></div>

<article class="abs t-card" style="left:803px">
  <span class="abs quote" style="left:16px;top:34px">“</span>
  <p class="abs t-text">Lorem ipsum dolor sit amet, consectetur adipiscing elit, sed do</p>
  <span class="abs quote" style="right:18px;top:150px">”</span>
  <div class="abs t-name">Mira Solden</div>
  <div class="abs t-stars">★★★★<span class="off">★</span></div>
</article>
<div class="abs avatar" style="left:887px" role="img" aria-label="Customer portrait"></div>

<!-- footer -->
<footer class="abs footer"></footer>
<div class="abs foot-brand"><span class="mark"></span>FERNBOLT</div>
<div class="abs contact-row" style="top:3492px">
  <svg width="26" height="26" viewBox="0 0 24 24"><path d="M6.6 10.8a15 15 0 0 0 6.6 6.6l2.2-2.2a1 1 0 0 1 1-.25 11.4 11.4 0 0 0 3.6.57 1 1 0 0 1 1 1V20a1 1 0 0 1-1 1A17 17 0 0 1 3 4a1 1 0 0 1 1-1h3.5a1 1 0 0 1 1 1c0 1.25.2 2.45.57 3.6a1 1 0 0 1-.25 1z" fill="#fff"/></svg>
  1-800-555-0142
</div>
<div class="abs contact-row small" style="top:3550px">
  <svg width="28" height="28" viewBox="0 0 28 28"><circle cx="14" cy="14" r="11" fill="none" stroke="#fff" stroke-width="2"/><path d="M14 7v7l5 3" fill="none" stroke="#fff" stroke-width="2"/></svg>
  Avaliable From 9am to 5Pm
</div>
<ul class="abs foot-col" style="left:561px">
  <li>Home</li><li>About</li><li>Products</li><li>Manufacturing</li><li>Products</li><li>contact</li><li>new arrivals</li>
</ul>
<ul class="abs foot-col" style="left:839px">
  <li>Terms $ Conditions</li><li>Returns</li><li>Pivacy policy</li><li>About Us</li><li>Contact Us</li><li>Sitemap</li>
</ul>
<p class="abs copyright">© 2020 All Rights Reserved | Privacy Policy | Terms and Conditions</p>
<div class="abs pay" aria-label="Accepted payment methods">
  <span style="background:#2a3a8c"></span>
  <span style="background:#e4572e"></span>
  <span style="background:#5d8fd6"></span>
  <span style="background:#dde6f3"></span>
</div>

</body>
</html>
```